New Business Card : Logo provided (black&red)

Use logo to ascertain colours.
Front of card :
Logo
Director : Darren Kellworth
ABN : 47302961
T : 0458 712 064
E : trimvolt@pelmarix.com
W : trimvoltfitness.net.au

Back of card :
Outdoor Group Training
Harrowvale Rowing Club
42 Pellinore Road
Scarborough WA 6019

Personal Training
Greywater Bay Fitness Studio
518 Marrowdene Street
Scarborough WA 6019

Logo's attached are low resolution apparently so will look into why that is and update as soon as I can.  

Logo's updated.

```html
<!DOCTYPE html>
<html lang="en">
<head>
<meta charset="utf-8">
<title>Trimvolt Fitness — Business Card</title>
<link rel="stylesheet" href="https://fonts.googleapis.com/css2?family=Didact+Gothic&family=Mulish:wght@700;800&display=swap">
<style>
  :root {
    --brand-red: #ee1d23;
    --card-red: #ab1012;
    --swoosh-grey: #6b6b6b;
    --border-grey: #9a9a9a;
    --ink: #1a1a1a;
    --paper: #ffffff;
    --reverse-text: #f4e4e4;
  }
  html, body {
    margin: 0;
    padding: 0;
    width: 781px;
    height: 1200px;
    overflow: hidden;
    background: var(--paper);
  }
  .sheet {
    position: relative;
    width: 781px;
    height: 1200px;
    font-family: "Didact Gothic", "Century Gothic", sans-serif;
    color: var(--ink);
  }

  /* Front face */
  .card-front {
    position: absolute;
    left: 0;
    top: 0;
    width: 767px;
    height: 437px;
    border: 2px solid var(--border-grey);
    background: var(--paper);
    overflow: hidden;
  }
  .card-front .swoosh {
    position: absolute;
    left: 0;
    top: 0;
    width: 767px;
    height: 437px;
  }
  .brand-lockup {
    position: absolute;
    left: 62px;
    top: 186px;
    display: flex;
    align-items: center;
    gap: 12px;
  }
  .brand-lockup .brand-dot {
    width: 30px;
    height: 30px;
    border-radius: 50%;
    background: var(--brand-red);
  }
  .brand-lockup .brand-name {
    font-family: "Mulish", "Century Gothic", sans-serif;
    font-weight: 800;
    font-size: 29px;
    letter-spacing: 0.5px;
    color: var(--ink);
    text-transform: uppercase;
  }
  .holder {
    position: absolute;
    left: 413px;
    top: 80px;
    width: 195px;
  }
  .holder .holder-name {
    margin: 0;
    font-family: "Mulish", "Century Gothic", sans-serif;
    font-weight: 700;
    font-size: 18.5px;
    color: var(--brand-red);
    text-transform: uppercase;
    white-space: nowrap;
  }
  .holder .holder-role {
    margin: 6px 0 0;
    text-align: right;
    font-family: "Mulish", "Century Gothic", sans-serif;
    font-weight: 700;
    font-size: 13px;
    text-transform: uppercase;
  }
  .rule {
    position: absolute;
    left: 362px;
    top: 131px;
    width: 350px;
    height: 6px;
    background: linear-gradient(to right, var(--brand-red) 0%, var(--brand-red) 35%, rgba(238, 29, 35, 0) 100%);
  }
  .contact-list {
    position: absolute;
    left: 413px;
    top: 169px;
    margin: 0;
    padding: 0;
    list-style: none;
    font-size: 15.5px;
    line-height: 30px;
  }
  .contact-list .label {
    font-family: "Mulish", "Century Gothic", sans-serif;
    font-weight: 700;
  }

  /* Back face */
  .card-back {
    position: absolute;
    left: 10px;
    top: 771px;
    width: 768px;
    height: 429px;
    background: var(--card-red);
    overflow: hidden;
    color: var(--reverse-text);
  }
  .card-back .emblem-ghost {
    position: absolute;
    left: 60px;
    top: 90px;
    width: 250px;
    height: 250px;
    border-radius: 50%;
    background: rgba(255, 255, 255, 0.18);
  }
  .locations {
    position: absolute;
    left: 398px;
    top: 100px;
    font-size: 15.5px;
    line-height: 18.3px;
  }
  .location {
    margin: 0 0 55px;
  }
  .location .service {
    margin: 0 0 18px;
  }
  .location address {
    font-style: normal;
  }
</style>
</head>
<body>
  <main class="sheet">
    <section class="card-front" aria-label="Business card front">
      <svg class="swoosh" viewBox="0 0 767 437" aria-hidden="true">
        <path d="M213 437 C 420 400, 640 360, 767 282 L767 437 Z" fill="var(--swoosh-grey)"/>
        <path d="M240 437 C 450 410, 650 360, 767 310 L767 437 Z" fill="var(--card-red)"/>
      </svg>

      <div class="brand-lockup">
        <span class="brand-dot" aria-hidden="true"></span>
        <span class="brand-name">Trimvolt Fitness</span>
      </div>

      <div class="holder">
        <p class="holder-name">Darren Kellworth</p>
        <p class="holder-role">Director</p>
      </div>
      <div class="rule" aria-hidden="true"></div>

      <ul class="contact-list">
        <li><span class="label">ABN :</span> 47302961</li>
        <li><span class="label">T :</span> 0458 712 064</li>
        <li><span class="label">E :</span> trimvolt@pelmarix.com</li>
        <li><span class="label">W :</span> trimvoltfitness.net.au</li>
      </ul>
    </section>

    <section class="card-back" aria-label="Business card back">
      <div class="emblem-ghost" aria-hidden="true"></div>
      <div class="locations">
        <div class="location">
          <p class="service">Outdoor Group Training</p>
          <address>Harrowvale Rowing Club<br>42 Pellinore Road<br>Scarborough WA 6019</address>
        </div>
        <div class="location">
          <p class="service">Personal Training</p>
          <address>Greywater Bay Fitness Studio<br>518 Marrowdene Street<br>Scarborough WA 6019</address>
        </div>
      </div>
    </section>
  </main>
</body>
</html>
```